Website for vegan focused blog

A website is needed so that I can launch my new blog in Dubai. It will be mainly vegan focused but also lifestyle based. Wordpress based- i started to build a site on Wordpress but design is not my forte ;)
Main content on the site will be; my recipes, reviews of products/restaurants, lifestyle posts and travel.
For this I ask for a homepage design, a recipe design page that includes a recipe card and a generic page for posts that can show pictures and videos. Also a contact me page.
Main headers should be: Home, Recipes and happy for suggestions.
Must look clean and neat but appealing, happy for minimalist look. I like pink and grey colours. Must be Wordpress compatible.
Have attached a couple of example posts for reference
Must have social links etc.
name of blog is: Marnie on the dunes
Other blogs I like are: https://tidyskillet.example/ https://shebrightens.example/ https://shebrightens.example/ https://www.ohladycakes.com/https://figsforsupper.example/ https://tessaborlow.example/

Target Market(s)

Residents in the UAE. General individuals interested in vegan meals, plant based nutrition, travel and reviews.

Number of Pages Required

4 page

Colors
eea4c8
eda3c7
f9d9e8
dbdbdb
aaaaaa
d5d5d5

Requirements
Must have
• Recipe page- must include recipe card plug in option
• Social media integration
• Email sign ups

```html
<!DOCTYPE html>
<html lang="en">
<head>
<meta charset="utf-8">
<title>Contact – Marnie on the dunes</title>
<link rel="stylesheet" href="https://fonts.googleapis.com/css2?family=Lato:wght@400;700&family=Playfair+Display:ital,wght@0,400;0,700;1,400;1,700&display=swap">
<style>
  :root {
    --pink: #eea4c8;
    --pink-strong: #e98fbb;
    --pink-soft: #f9d9e8;
    --line: #dbdbdb;
    --line-soft: #ececec;
    --muted: #aaaaaa;
    --text: #555555;
    --dark: #444444;
    --footer-bg: #f8f8f8;
    --white: #ffffff;
  }
  * { box-sizing: border-box; margin: 0; padding: 0; }
  html, body { width: 1200px; height: 1110px; overflow: hidden; background: var(--white); }
  body { position: relative; font-family: "Lato", sans-serif; color: var(--text); }

  .site-header { position: absolute; left: 0; top: 0; width: 1200px; height: 115px; border-bottom: 1px solid var(--line-soft); }
  .brand { position: absolute; left: 0; width: 1200px; text-align: center; font-family: "Playfair Display", serif; font-weight: 400; color: var(--pink); white-space: nowrap; }
  .site-header .brand { top: 40px; font-size: 36px; line-height: 44px; }

  .main-nav { position: absolute; left: 0; top: 115px; width: 1200px; height: 38px; }
  .main-nav a { position: absolute; top: 12px; font-family: "Playfair Display", serif; font-style: italic; font-weight: 700; font-size: 11px; line-height: 14px; color: var(--dark); text-decoration: none; letter-spacing: .2px; white-space: nowrap; }
  .main-nav a.is-active { color: var(--pink); }
  .search-icon { position: absolute; left: 954px; top: 13px; }

  .map-area { position: absolute; left: 0; top: 153px; width: 1200px; height: 321px;
    background: linear-gradient(90deg, #8eb0cf 0%, #8fb0cd 32%, #c9c9c9 42%, #c6c6c6 65%, #9fbbd6 80%, #c4c4c4 100%); }

  .contact-card { position: absolute; left: 234px; top: 240px; width: 367px; height: 153px; background: rgba(255,255,255,.94); box-shadow: 0 2px 8px rgba(0,0,0,.12); }
  .contact-card .photo { position: absolute; left: 0; top: 0; width: 125px; height: 153px;
    background: linear-gradient(160deg, #3a3234 0%, #5b3b31 40%, #c94a23 70%, #2b2526 100%); }
  .contact-list { position: absolute; left: 159px; top: 39px; list-style: none; }
  .contact-list li { position: relative; padding-left: 24px; font-size: 10.5px; font-weight: 700; color: var(--text); line-height: 12px; margin-bottom: 15px; white-space: nowrap; }
  .contact-list svg { position: absolute; left: 0; top: 0; }

  .touch { position: absolute; left: 233px; top: 523px; width: 740px; }
  .touch h1 { font-family: "Playfair Display", serif; font-weight: 700; font-size: 28px; color: var(--pink); line-height: 36px; }
  .touch p { margin-top: 4px; margin-left: 2px; font-size: 10px; line-height: 15px; color: var(--text); }

  .field { position: absolute; border: 1px solid var(--line); background: var(--white); font-size: 8.5px; color: #888; padding-left: 24px; line-height: 23px; }
  .field svg { position: absolute; left: 9px; top: 7px; }
  .btn-send { position: absolute; left: 234px; top: 823px; width: 90px; height: 24px; background: var(--pink); color: var(--white); font-family: "Lato", sans-serif; font-weight: 700; font-size: 8.5px; letter-spacing: .6px; text-align: center; line-height: 24px; border: 0; }

  .site-footer { position: absolute; left: 0; top: 909px; width: 1200px; height: 201px; background: var(--footer-bg); }
  .site-footer .brand { top: 40px; font-size: 30px; line-height: 38px; }
  .social { position: absolute; top: 112px; left: 526px; display: flex; gap: 9px; }
  .social span { width: 22px; height: 22px; border-radius: 50%; background: var(--pink); display: block; }
  .footer-rule { position: absolute; left: 0; top: 163px; width: 1200px; border-top: 1px solid var(--line-soft); }
  .copyright { position: absolute; left: 0; top: 177px; width: 1200px; text-align: center; font-size: 8px; color: var(--muted); }
</style>
</head>
<body>
  <header class="site-header">
    <div class="brand">Marnie on the dunes</div>
  </header>

  <nav class="main-nav">
    <a style="left:337px">Home</a>
    <a style="left:401px">About</a>
    <a class="is-active" style="left:468px">Recipes</a>
    <a style="left:542px">Reviews of products</a>
    <a style="left:678px">Lifestyle</a>
    <a style="left:757px">Travel</a>
    <a style="left:826px">Contact</a>
    <svg class="search-icon" width="12" height="12" viewBox="0 0 12 12"><circle cx="5" cy="5" r="3.8" fill="none" stroke="#555" stroke-width="1.6"/><path d="M8 8l3 3" stroke="#555" stroke-width="1.8" stroke-linecap="round"/></svg>
  </nav>

  <div class="map-area" role="img" aria-label="Street map of the city centre with the coastline and creek"></div>

  <section class="contact-card">
    <div class="photo" role="img" aria-label="City street between tall buildings at sunset"></div>
    <ul class="contact-list">
      <li><svg width="11" height="11" viewBox="0 0 11 11"><path d="M2 1l2 2.5-1 1.2c.7 1.4 1.8 2.5 3.2 3.2l1.2-1L10 9l-1.2 1.5C5 10 1 6 .6 2.2z" fill="none" stroke="#eea4c8" stroke-width=".9"/></svg>04 555 01 92</li>
      <li><svg width="12" height="10" viewBox="0 0 12 10"><rect x=".5" y="1" width="11" height="8" fill="none" stroke="#eea4c8"/><path d="M.5 1.5l5.5 4 5.5-4" fill="none" stroke="#eea4c8"/></svg>marnie@dunesmail.example</li>
      <li><svg width="10" height="12" viewBox="0 0 10 12"><path d="M5 11.5S1 7 1 4.5a4 4 0 018 0C9 7 5 11.5 5 11.5z" fill="none" stroke="#eea4c8"/><circle cx="5" cy="4.5" r="1.4" fill="none" stroke="#eea4c8"/></svg>1234 Lorem Ipsum Dolor Sit<br>Magna tempus - Interdum</li>
    </ul>
  </section>

  <section class="touch">
    <h1>Get In Touch</h1>
    <p>Ut a lorem finibus urna tincidunt lacinia. Nullam hendrerit, nisl in elementum rutrum, sapien quam pellentesque mauris, nec cursus nulla nisi sed mi.<br>Quisque et purus volutpat, maximus dolor quis, aliquet turpis.</p>
  </section>

  <form>
    <div class="field" style="left:234px;top:626px;width:356px;height:25px"><svg width="9" height="9" viewBox="0 0 9 9"><circle cx="4.5" cy="3" r="2" fill="none" stroke="#eea4c8" stroke-width=".8"/><path d="M1 8.5c.5-2 2-3 3.5-3s3 1 3.5 3z" fill="none" stroke="#eea4c8" stroke-width=".8"/></svg>Your name</div>
    <div class="field" style="left:609px;top:626px;width:356px;height:25px"><svg width="9" height="9" viewBox="0 0 11 11"><path d="M2 1l2 2.5-1 1.2c.7 1.4 1.8 2.5 3.2 3.2l1.2-1L10 9l-1.2 1.5C5 10 1 6 .6 2.2z" fill="none" stroke="#eea4c8"/></svg>Your phone</div>
    <div class="field" style="left:234px;top:667px;width:356px;height:25px"><svg width="9" height="8" viewBox="0 0 12 10"><rect x=".5" y="1" width="11" height="8" fill="none" stroke="#eea4c8"/><path d="M.5 1.5l5.5 4 5.5-4" fill="none" stroke="#eea4c8"/></svg>Your email</div>
    <div class="field" style="left:609px;top:667px;width:356px;height:25px"><svg width="9" height="9" viewBox="0 0 9 9"><path d="M1 8l1-3 5-4.5 1.5 1.5L4 7z" fill="none" stroke="#eea4c8" stroke-width=".8"/></svg>Subject</div>
    <div class="field" style="left:234px;top:707px;width:731px;height:100px"><svg width="9" height="8" viewBox="0 0 9 8"><path d="M.5.5h8v5H3L1 7.5v-2H.5z" fill="none" stroke="#eea4c8" stroke-width=".8"/></svg>Your message</div>
    <button class="btn-send" type="button">SEND MESSAGE</button>
  </form>

  <footer class="site-footer">
    <div class="brand">Marnie on the dunes</div>
    <div class="social" aria-label="Social profiles">
      <span aria-label="Social profile 1"></span>
      <span aria-label="Social profile 2"></span>
      <span aria-label="Social profile 3"></span>
      <span aria-label="Social profile 4"></span>
      <span aria-label="Social profile 5"></span>
    </div>
    <div class="footer-rule"></div>
    <p class="copyright">Copyright © 2018 Marnie on the dunes. All Right Reserved. Privacy Policy | Terms of Service</p>
  </footer>
</body>
</html>
```